Brightfold Systems - IT Service and Consulting
Business Card, Letterhead, Envelopes, Fax templates, and CD Label
Brightfold Systems - IT Service and Consulting -
Creative Brief
Professional
Mara Pellin
Owner
517 W. Orchard Gate Ave #216 Orchard Gate, CA 90482
MPellin@BrightfoldSystems.Com
www.brightfoldsystems.com
We want to communicate that Brightfold Systems is a professional IT Service and Consulting Firm. We want a stationary that conveys professionalism and confidence, at the same time we want to appear unique and approachable to small businesses.
Back should be used to convey the company logo, tagline, and URL.

```html
<!DOCTYPE html>
<html lang="en">
<head>
<meta charset="utf-8">
<title>Brightfold Systems – Business Card</title>
<link rel="stylesheet" href="https://fonts.googleapis.com/css2?family=Jost:wght@400;500;600&display=swap">
<style>
  :root {
    --page-bg: #e9ebee;
    --brand-blue: #1c5cb5;
    --brand-blue-deep: #13479a;
    --brand-blue-light: #2a6fcc;
    --card-white: #ffffff;
    --divider-grey: #d3d6db;
    --text-dark: #20344f;
    --text-white: #ffffff;
    --text-soft: #c9dbf5;
  }
  * { box-sizing: border-box; margin: 0; padding: 0; }
  html, body { width: 1200px; height: 901px; overflow: hidden; }
  body {
    background: var(--page-bg);
    font-family: "Jost", "Helvetica Neue", Arial, sans-serif;
    position: relative;
  }
  .card {
    position: absolute;
    left: 250px;
    width: 700px;
    height: 400px;
    overflow: hidden;
    box-shadow: 0 10px 30px rgba(20, 40, 80, 0.18);
  }

  /* Back of card */
  .card-back {
    top: 30px;
    background: linear-gradient(160deg, var(--brand-blue-light) 0%, var(--brand-blue) 55%, var(--brand-blue-deep) 100%);
    color: var(--text-white);
  }
  .card-back .back-identity {
    position: absolute;
    right: 60px;
    top: 130px;
    text-align: right;
  }
  .card-back .company-name {
    font-size: 52px;
    font-weight: 600;
    letter-spacing: -0.5px;
    line-height: 1;
  }
  .card-back .tagline {
    margin-top: 10px;
    font-size: 15px;
    font-weight: 500;
    letter-spacing: 5px;
    color: var(--text-soft);
  }
  .card-back .website {
    margin-top: 34px;
    font-size: 16px;
    letter-spacing: 1.5px;
    color: var(--text-soft);
  }

  /* Front of card */
  .card-front {
    top: 470px;
    background: var(--card-white);
  }
  .front-top {
    position: absolute;
    left: 0; top: 0;
    width: 100%; height: 250px;
    background: linear-gradient(180deg, #ffffff 0%, #f2f3f5 100%);
  }
  .front-logo {
    position: absolute;
    left: 80px;
    top: 58px;
    display: flex;
    align-items: center;
    gap: 20px;
  }
  .logo-dot {
    width: 78px; height: 78px;
    border-radius: 50%;
    background: var(--brand-blue);
    flex: none;
  }
  .front-logo .company-name {
    font-size: 50px;
    font-weight: 600;
    color: var(--brand-blue);
    line-height: 1;
    letter-spacing: -0.5px;
  }
  .front-logo .tagline {
    margin-top: 8px;
    font-size: 13px;
    font-weight: 500;
    letter-spacing: 4px;
    color: var(--text-dark);
  }
  .person {
    position: absolute;
    left: 180px;
    top: 196px;
    font-size: 20px;
    color: var(--brand-blue);
  }
  .person .person-name { font-weight: 600; }
  .person .person-sep { margin: 0 12px; color: #8a97aa; }
  .person .person-role { font-weight: 400; color: #5a6a82; font-size: 17px; }

  .front-divider {
    position: absolute;
    left: 0; top: 250px;
    width: 100%; height: 8px;
    background: var(--divider-grey);
  }
  .front-bottom {
    position: absolute;
    left: 0; top: 258px;
    width: 100%; height: 142px;
    background: linear-gradient(180deg, var(--brand-blue-light) 0%, var(--brand-blue) 100%);
    color: var(--text-white);
  }
  .address {
    position: absolute;
    left: 78px;
    top: 46px;
    font-size: 17px;
    line-height: 1.5;
    text-align: right;
    width: 290px;
  }
  .contact-rule {
    position: absolute;
    left: 392px;
    top: 42px;
    width: 1px;
    height: 58px;
    background: rgba(255,255,255,0.6);
  }
  .contacts {
    position: absolute;
    left: 410px;
    top: 46px;
    font-size: 17px;
    line-height: 1.5;
  }
  .contact-line { display: flex; align-items: center; gap: 10px; }
  .contact-line svg { width: 16px; height: 16px; flex: none; }
</style>
</head>
<body>

  <section class="card card-back" aria-label="Business card back">
    <div class="back-identity">
      <div class="company-name">Brightfold Systems</div>
      <div class="tagline">CLEAR ANSWERS FOR BUSY TEAMS</div>
      <div class="website">www.brightfoldsystems.com</div>
    </div>
  </section>

  <section class="card card-front" aria-label="Business card front">
    <div class="front-top">
      <div class="front-logo">
        <div class="logo-dot"></div>
        <div>
          <div class="company-name">Brightfold Systems</div>
          <div class="tagline">CLEAR ANSWERS FOR BUSY TEAMS</div>
        </div>
      </div>
      <div class="person">
        <span class="person-name">Mara Pellin</span><span class="person-sep">/</span><span class="person-role">Owner</span>
      </div>
    </div>
    <div class="front-divider"></div>
    <div class="front-bottom">
      <div class="address">
        517 W. Orchard Gate Ave #216<br>
        Orchard Gate, CA 90482
      </div>
      <div class="contact-rule"></div>
      <div class="contacts">
        <div class="contact-line">
          <svg viewBox="0 0 16 16" aria-hidden="true"><path d="M3.5 1.5l2.5 0 1 3.5-1.6 1.2c.8 1.8 2.2 3.2 4 4l1.2-1.6 3.5 1v2.5c0 .8-.7 1.4-1.5 1.4C6.8 13.5 2.5 9.2 2.1 3 2.1 2.2 2.7 1.5 3.5 1.5z" fill="#ffffff"/></svg>
          <span>626-555-0193</span>
        </div>
        <div class="contact-line">
          <svg viewBox="0 0 16 16" aria-hidden="true"><rect x="1.5" y="3.5" width="13" height="9" fill="none" stroke="#ffffff" stroke-width="1.4"/><path d="M1.5 3.5L8 9l6.5-5.5" fill="none" stroke="#ffffff" stroke-width="1.4"/></svg>
          <span>MPellin@BrightfoldSystems.Com</span>
        </div>
      </div>
    </div>
  </section>

</body>
</html>
```